RVT 2023 Postcard

We need a postcard created for an upcoming trade show. We had something made for our sister company a while back and are interested in a similar look. We have included images and some layouts that can be used along with our logo. We like earthy colors, gray and black are okay too. We would like it to be 5x7 and landscape orientation. We have attached the wording we would like to see on the back of the card with changes made in red.
Target Market(s)
retailers
Industry/Entity Type
wedding ring
Colors
Designer to choose only greyscale colors for use in the design.
Look and feel

```html
<!DOCTYPE html>
<html lang="en">
<head>
<meta charset="utf-8">
<title>RVT 2023 Postcard</title>
<link rel="stylesheet" href="https://fonts.googleapis.com/css2?family=Cinzel:wght@400;600&family=Poppins:ital,wght@0,300;0,400;0,600;1,400;1,700&display=swap">
<style>
  :root {
    --page: #d3d3d3;
    --black: #000000;
    --card-dark: #161616;
    --card-mid: #2b2b2b;
    --grey-heading: #8d8d8d;
    --grey-band: #6e6e6e;
    --grey-logo: #8a8a8a;
    --text-light: #e6e6e6;
    --text-soft: #bdbdbd;
    --tile: #ffffff;
  }
  * { box-sizing: border-box; margin: 0; padding: 0; }
  html, body { width: 720px; height: 1200px; overflow: hidden; }
  body { background: var(--page); font-family: "Poppins", sans-serif; position: relative; }

  .postcard {
    position: absolute; width: 640px; height: 457px; overflow: hidden;
    box-shadow: 4px 5px 10px rgba(0,0,0,.35);
  }
  .postcard--front { left: 30px; top: 70px; background: radial-gradient(ellipse at 45% 50%, #2a2a2a 0%, #0b0b0b 55%, #000 100%); }
  .postcard--back { left: 50px; top: 650px; background: linear-gradient(160deg, var(--card-mid) 0%, var(--card-dark) 100%); }

  .photo { position: absolute; }
  .front-photo--stones { left: 88px; top: 53px; width: 294px; height: 161px; border-radius: 147px 147px 10px 10px;
    background: radial-gradient(ellipse at 50% 40%, #7a7068 0%, #4d4640 60%, #2c2825 100%); }
  .front-photo--marble { left: 258px; top: 245px; width: 295px; height: 160px; border-radius: 10px 10px 147px 147px;
    background: radial-gradient(ellipse at 50% 40%, #e2e2e0 0%, #b8b6b2 60%, #8f8c88 100%); }

  .brand { position: absolute; display: flex; flex-direction: column; align-items: center; color: var(--grey-logo); font-family: "Poppins", sans-serif; font-weight: 400; text-align: center; }
  .brand__square { width: 90px; height: 90px; background: var(--grey-logo); }
  .brand__name { margin-top: 6px; letter-spacing: .08em; line-height: 1.15; }
  .postcard--front .brand { left: 436px; top: 67px; }
  .postcard--front .brand__name { font-size: 15px; }
  .postcard--back .brand { left: 508px; top: 14px; }
  .postcard--back .brand__square { width: 68px; height: 68px; }
  .postcard--back .brand__name { font-size: 12px; }

  .back-title { position: absolute; left: 10px; top: 24px; font-family: "Cinzel", serif; font-weight: 600; font-size: 20.5px; color: var(--grey-heading); text-decoration: underline; text-decoration-thickness: 1px; text-underline-offset: 3px; letter-spacing: .01em; }
  .back-lead { position: absolute; left: 10px; top: 62px; font-size: 13.5px; font-weight: 400; color: var(--text-light); }

  .feature-list { position: absolute; left: 13px; top: 96px; list-style: none; }
  .feature-list li { display: flex; align-items: center; height: 23px; font-size: 12.5px; font-weight: 300; color: var(--text-soft); }
  .feature-list li::before { content: ""; width: 8px; height: 8px; border-radius: 50%; border: 1px solid #555; margin-right: 12px; }

  .band { position: absolute; left: 0; display: flex; align-items: center; padding-left: 35px; }
  .band--tagline { top: 226px; width: 351px; height: 26px; background: var(--black); color: #fff; font-weight: 600; font-size: 14px; }
  .band--call { top: 253px; width: 345px; height: 25px; background: var(--grey-band); color: #fff; font-style: italic; font-size: 14px; }
  .band--call strong { font-weight: 700; font-size: 15.5px; margin: 0 4px; }

  .perks { position: absolute; left: 35px; top: 293px; width: 330px; display: grid; grid-template-columns: 194px 136px; row-gap: 9px; list-style: none; }
  .perks li { font-size: 9.5px; font-weight: 300; color: var(--text-soft); letter-spacing: .01em; }
  .perks li::before { content: "• "; }

  .contact { position: absolute; left: 0; top: 388px; width: 377px; height: 34px; background: rgba(0,0,0,.75); padding: 5px 0 0 35px; color: #fff; font-size: 9px; line-height: 13px; }
  .social { position: absolute; left: 35px; top: 431px; display: flex; align-items: center; color: #fff; font-size: 9px; }
  .social__dot { width: 8px; height: 8px; border-radius: 50%; background: #4b6fb6; margin-right: 5px; }

  .ring-strip { position: absolute; left: 411px; top: 129px; width: 229px; height: 328px; background: var(--black); }
  .tile { position: absolute; background: var(--tile); }
  .back-photo--stone { left: 411px; top: 140px; width: 229px; height: 112px; background: linear-gradient(180deg, #9a8f84 0%, #7a6c5f 60%, #5d5148 100%); }
  .back-photo--white { background: radial-gradient(ellipse at 50% 50%, #d8d8d8 0%, #f4f4f4 45%, #fff 70%); }
  .back-photo--rose { background: radial-gradient(ellipse at 50% 50%, #e2aa96 0%, #f3ddd4 45%, #fff 70%); }
  .back-photo--gold { background: radial-gradient(ellipse at 50% 50%, #e6c35a 0%, #f5e6b4 45%, #fff 70%); }
</style>
</head>
<body>

<section class="postcard postcard--front" aria-label="Postcard front">
  <div class="photo front-photo--stones" role="img" aria-label="Wedding bands in rose, white and yellow gold resting on grey pebbles and a stone"></div>
  <div class="photo front-photo--marble" role="img" aria-label="Two brushed white gold bands standing on a pale marble surface"></div>
  <div class="brand">
    <span class="brand__square"></span>
    <span class="brand__name">HALDEN RINGS</span>
  </div>
</section>

<section class="postcard postcard--back" aria-label="Postcard back">
  <h1 class="back-title">PREMIUM CUSTOMIZED PROGRAMS</h1>
  <p class="back-lead">Promote your own brand, rings stamped with your specified logo.</p>
  <ul class="feature-list">
    <li>Offer rings in any width, 3 thicknesses and all precious metals</li>
    <li>Combine &amp; customize 5500 ring designs.</li>
    <li>Sell in Platinum, 18kt, 14kt &amp; 10kt</li>
    <li>Samples kits starting as low as $900 Program</li>
    <li>Performance Money Back Guarante</li>
  </ul>

  <div class="band band--tagline">YOUR TRUSTED SOURCE FOR RINGS</div>
  <div class="band band--call">Call <strong>800-555-0142</strong> for information</div>

  <ul class="perks">
    <li>EASY PRICING SYSTEM</li>
    <li>FREE SHIPPING</li>
    <li>SCRAP BUYOUT OPTIONS</li>
    <li>PRE-TAGGED SAMPLES</li>
    <li>1 WEEK TURNAROUND</li>
    <li>COMPETITIVE PRICING</li>
    <li>FAMILY OWNED AND OPERATED</li>
    <li>MADE PROUDLY IN THE USA</li>
  </ul>

  <address class="contact" style="font-style:normal">
    410 Meadow Lane, Glen Falls NY 12801<br>
    Ph: 800-555-0142 &nbsp;|&nbsp; E: sales@haldenrings.com &nbsp;|&nbsp; www.haldenrings.com
  </address>
  <div class="social"><span class="social__dot"></span>GoHaldenRings</div>

  <div class="brand">
    <span class="brand__square"></span>
    <span class="brand__name">HALDEN RINGS</span>
  </div>

  <div class="ring-strip"></div>
  <div class="photo back-photo--stone" role="img" aria-label="Row of white, two-tone and yellow gold bands on a stone ledge"></div>
  <div class="tile back-photo--white" style="left:411px;top:258px;width:82px;height:112px" role="img" aria-label="White gold band with engraved leaf pattern"></div>
  <div class="tile back-photo--rose" style="left:500px;top:258px;width:140px;height:112px" role="img" aria-label="Rose gold band set with a small diamond"></div>
  <div class="tile back-photo--gold" style="left:411px;top:377px;width:145px;height:80px" role="img" aria-label="Polished yellow gold band"></div>
  <div class="tile back-photo--white" style="left:562px;top:377px;width:78px;height:38px" role="img" aria-label="Textured white gold band"></div>
  <div class="tile back-photo--rose" style="left:562px;top:420px;width:78px;height:37px" role="img" aria-label="White and rose gold band"></div>
</section>

</body>
</html>
```